World's first Total Sustainability Management System needs brochure

DESIGN BRIEF
1. HISTORY
The company is a new company but has very quickly gained global recognition by international bodies such as the WCO and is already operating globally.
2. PROBLEM STATEMENT + MESSAGE
The system provides management of a wide range of problems in the business, and a significant number of benefits from reduced costs, to better risk management, improved compliance, recognition, differentiation strategy, reporting etc.
Halcyon Ledger needs to communicate this message simply.
The target audience is industry leaders WHO ARE ALREADY commited to CSR/ Sustainability.
The message is that Halcyon Ledger can help them do it better, reduce costs, improve risk management and provide them with a return on their investment in sustainability/ social resonsibility.
Website: www.hlassurance-example.com
3. GOALS
To position Halcyon Ledger as distinct, elite management system. It is much much more than a mere reporting system or corporate giving program. Rather, it provides management with a whole strategy and range of tools for managing the soft side of the business.
4. DESIRED TEXT
What does sustainability or social investment mean to you?
Many businesses see it as charitable giving or an annual report or an environmental program. International best practice describes it more broadly and comprehensively. It includes such things as workplace safety, anti-corruption and labour.
What do you currently receive for your social investment?
a) report
b) community recognition
c) certificate
Can you do it better and get a better return on your social investment?
The Halcyon Ledger CSR Management System is built specifically to enhance business performance using socially responsibility principles. It not only provides reporting, recognition, certification, but provides a return on investment. It is web based system, provides complete management system and comprehensive framework to drive improvement and social responsibility throughout your business.
Halcyon Ledger, a WCO recognised business, provides a comprehensive system for embedding performance enhancing world best practices into your business.

5. COLLATERAL
We would like to see this on a double sided A4 sheet of paper (or 8 ½ x 11)

Isn’t it time you joined world leaders?
Halcyon Ledger Assurance Systems
47 Quarry Rd, Elmwick, Vic or 38 Finch Court, London, UK WC9Z 4QJ
Email: info@hlassurance-example.com Email: info@hlassurance-example.com
Phone: +61 3 5049-2387 +44 (0) 20 3815 6027

Reason: The original design brief was inadequate--my apologies. Please have a look and see if this works better for you.

Hello, I have added some details which were unavailable before and committed the funding to the project. Thanks for your interest.

Target Market(s)

This brochure is designed for CEO's and other top level executives who are knowledgeable and interested in social responsibility and sustainability. They are middle aged, are all well educated and socially concerned.

Industry/Entity Type

Sustainability

Font styles to use
Sans Serif

Requirements
Must have
• Must be 2 sided A4 (8.5 x 11).
PLEASE SEE WEBSITE FOR ADDITIONAL INFORMATION www.hlassurance-example.com
Should not have
• It should not over emphasise green/ environmental issues.

```html
<!DOCTYPE html>
<html lang="en">
<head>
<meta charset="utf-8">
<title>Halcyon Ledger Assurance Systems – Brochure</title>
<link rel="stylesheet" href="https://fonts.googleapis.com/css2?family=Open+Sans:ital,wght@0,400;0,600;0,700;1,600&display=swap">
<style>
:root{
  --blue:#1b63ad;
  --teal:#17a9b8;
  --green:#9ccc4a;
  --orange:#f0901e;
  --ink:#4a4a4a;
  --paper:#ffffff;
  --stage:#3a3a3a;
  --tri-light:#d7eef5;
  --tri-mid:#8fcbe0;
}
*{box-sizing:border-box;margin:0;padding:0}
html,body{width:1200px;height:826px;overflow:hidden;background:var(--stage)}
body{font-family:"Open Sans",Arial,sans-serif;color:var(--ink)}
.canvas{position:relative;width:1200px;height:826px}
.page{position:absolute;top:68px;width:486px;height:626px;background:var(--paper);overflow:hidden}
.page--front{left:90px}
.page--back{left:632px}
.abs{position:absolute}

/* header photo */
.hero{left:0;top:0;width:486px;height:100px;
  background:linear-gradient(100deg,#5d8fc7 0%,#9fc4e4 35%,#cfe6d2 60%,#8cc451 80%,#4f9a2e 100%)}
.hero__banner{left:54px;top:46px;width:384px;height:34px;border:1px solid rgba(255,255,255,.85);
  background:rgba(23,169,184,.75);color:#fff;font-style:italic;font-weight:600;font-size:13px;
  display:flex;align-items:center;justify-content:center}

.stripes{left:0;width:486px;height:8px;display:flex}
.stripes span{flex:1}
.stripes .s1{background:var(--blue)}
.stripes .s2{background:var(--teal)}
.stripes .s3{background:var(--green)}
.stripes .s4{background:var(--orange)}

/* brand row */
.brand-tag{left:26px;top:157px;font-size:8px;color:#555}
.brand-name{left:25px;top:166px;font-size:26px;font-weight:700;color:var(--blue);line-height:1}
.brand-sub{left:110px;top:196px;font-size:7.5px;color:#666}
.logo{left:292px;top:162px;display:flex;align-items:center;gap:8px}
.logo__mark{width:32px;height:32px;background:var(--teal)}
.logo__name{font-size:15px;font-weight:700;color:var(--blue);line-height:1.05}

/* numbered sections */
.section{left:26px;display:flex;gap:18px;width:440px}
.num{flex:none;width:44px;height:44px;color:#fff;font-size:38px;font-weight:400;line-height:44px;text-align:center}
.num--orange{background:var(--orange)}
.num--blue{background:var(--blue)}
.num--teal{background:var(--teal)}
.num--green{background:var(--green)}
.section__body{width:378px}
.section__title{font-size:13px;font-weight:700;color:var(--blue);letter-spacing:1px;line-height:1.1;margin-bottom:3px}
.section__text{font-size:9.4px;line-height:13.4px;text-align:justify}
.section__text p{margin:0}
.link{font-weight:700;color:var(--blue)}
.choices{margin:5px 0 6px;font-weight:700;color:var(--blue);font-size:10px;line-height:16px}

/* decorative triangle fields */
.mosaic{position:absolute}

/* contact */
.contact{left:20px;top:462px;font-size:6.6px;line-height:8.4px;color:#555}
.contact__brand{display:flex;align-items:center;gap:5px;margin-bottom:6px}
.contact__mark{width:14px;height:14px;background:var(--teal)}
.contact__name{font-size:10px;font-weight:700;color:var(--blue)}
.contact__city{font-weight:700;color:var(--blue);font-size:7.5px;margin-top:4px}
.contact .tel{color:var(--blue);font-weight:600}
.people{left:208px;top:470px;width:270px;height:132px}
</style>
</head>
<body>
<div class="canvas">

  <!-- FRONT -->
  <section class="page page--front">
    <div class="abs hero" role="img" aria-label="Photo of wind turbines against a blue sky with fresh green leaves"></div>
    <div class="abs hero__banner">Improving Business Performance Through Social Responsibility</div>
    <div class="abs stripes" style="top:100px"><span class="s1"></span><span class="s2"></span><span class="s3"></span><span class="s4"></span></div>

    <div class="abs brand-tag">Improve your Business Performance with</div>
    <div class="abs brand-name">Halcyon Ledger</div>
    <div class="abs brand-sub">Assurance Systems</div>
    <div class="abs logo">
      <span class="logo__mark"></span>
      <span class="logo__name">Halcyon Ledger<br>Assurance Systems</span>
    </div>

    <div class="abs section" style="top:238px">
      <div class="num num--orange">1</div>
      <div class="section__body">
        <h2 class="section__title">HISTORY</h2>
        <div class="section__text"><p>The company is a new company but has very quickly gained global recognition by international bodies such as the WCO and is already operating globally.</p></div>
      </div>
    </div>

    <div class="abs section" style="top:318px">
      <div class="num num--blue">2</div>
      <div class="section__body">
        <h2 class="section__title">PROBLEM STATEMENT + MESSAGE</h2>
        <div class="section__text">
          <p>The system provides management of a wide range of problems in the business, and a significant number of benefits from reduced costs, to better risk management, improved compliance, recognition, differentiation strategy, reporting etc.</p>
          <p>Halcyon Ledger needs to communicate this message simply.</p>
          <p>The target audience is industry leaders WHO ARE ALREADY commited to CSR/ Sustainability.</p>
          <p>The message is that Halcyon Ledger can help them do it better, reduce costs, improve risk management and provide them with a return on their investment in sustainability/ social resonsibility.</p>
          <p class="link">Website: www.hlassurance-example.com</p>
        </div>
      </div>
    </div>

    <svg class="mosaic" style="left:0;top:490px" width="486" height="136" viewBox="0 0 486 136" role="img" aria-label="Decorative field of light blue triangles">
      <defs>
        <linearGradient id="triFront" x1="0" y1="0" x2="0" y2="1">
          <stop offset="0" stop-color="#d7eef5"/>
          <stop offset="1" stop-color="#8fcbe0"/>
        </linearGradient>
      </defs>
      <polygon points="0,60 70,40 150,70 220,10 300,30 360,60 430,40 486,55 486,136 0,136" fill="url(#triFront)"/>
    </svg>
  </section>

  <!-- BACK -->
  <section class="page page--back">
    <svg class="mosaic" style="left:0;top:0" width="486" height="110" viewBox="0 0 486 110" role="img" aria-label="Decorative field of light blue triangles">
      <defs>
        <linearGradient id="triBack" x1="0" y1="0" x2="1" y2="0">
          <stop offset="0" stop-color="#b7e0ee"/>
          <stop offset="1" stop-color="#e2f3f8"/>
        </linearGradient>
      </defs>
      <polygon points="0,0 486,0 486,100 400,80 330,50 260,30 150,22 60,14 0,18" fill="url(#triBack)"/>
    </svg>

    <div class="abs section" style="top:88px">
      <div class="num num--teal">3</div>
      <div class="section__body">
        <h2 class="section__title">GOALS</h2>
        <div class="section__text"><p>To position Halcyon Ledger as distinct, elite management system. It is much much more than a mere reporting system or corporate giving program. Rather, it provides management with a whole strategy and range of tools for managing the soft side of the business.</p></div>
      </div>
    </div>

    <div class="abs section" style="top:174px">
      <div class="num num--green">4</div>
      <div class="section__body">
        <h2 class="section__title">DESIRED TEXT</h2>
        <div class="section__text">
          <p>What does sustainability or social investment mean to you?</p>
          <p>Many businesses see it as charitable giving or an annual report or an environmental program. International best practice describes it more broadly and comprehensively. It includes such things as workplace safety, anti-corruption and labour.</p>
          <p>What do you currently receive for your social investment?</p>
          <div class="choices">a) report<br>b) community recognition<br>c) certificate</div>
          <p>Can you do it better and get a better return on your social investment?</p>
          <p>The Halcyon Ledger CSR Management System is built specifically to enhance business performance using socially responsibility principles. It not only provides reporting, recognition, certification, but provides a return on investment. It is web based system, provides complete management system and comprehensive framework to drive improvement and social responsibility throughout your business.</p>
          <p>Halcyon Ledger, a WCO recognised business, provides a comprehensive system for embedding performance enhancing world best practices into your business.</p>
        </div>
      </div>
    </div>

    <div class="abs contact">
      <div class="contact__brand"><span class="contact__mark"></span><span class="contact__name">Halcyon Ledger</span></div>
      <div class="contact__city">Melbourne</div>
      Halcyon Ledger Assurance Systems<br>
      47 Quarry Road<br>
      Elmwick, Victoria, Australia 3187<br>
      Telephone: <span class="tel">+61 (0) 3 5049 2387</span><br>
      Email: info@hlassurance-example.com
      <div class="contact__city">London</div>
      Halcyon Ledger Assurance Systems<br>
      38 Finch Court<br>
      London, UK WC9Z 4QJ<br>
      Telephone: <span class="tel">+44 (0) 20 3815 6027</span><br>
      Email: info@hlassurance-example.com
    </div>

    <div class="abs people" role="img" aria-label="Business people standing on a teal world map"
         style="background:radial-gradient(ellipse at 50% 70%,#7fd0cf 0%,#c5ecec 45%,#ffffff 75%)"></div>

    <div class="abs stripes" style="top:612px;height:14px"><span class="s1"></span><span class="s2"></span><span class="s3"></span><span class="s4"></span></div>
  </section>

</div>
</body>
</html>
```